Design website for new email startup

We are starting a company called Ravo.QT (it will live at http://ravo.qt.example).

We would like the main landing page for our site designed. We have provided a very simple wireframe to help provide direction for the content it should include, but we do not expect the designers to adhere to it at all - we encourage unique ideas. There is some sample text in the wireframe - this does not have to be used, but may provide ideas.

We provide an easy way for people to manage email for a custom domain name. For example if you own "myhomeplace.example" you can point your DNS records to us and we'll make it easy to have emails addressed to your domain get forwarded to your existing email (gmail, etc). Folks running blogs, and other small sites can quickly setup email addresses for their domains and manage them in one place.

(For technical folks, we have you point your dns mx records to us, hence the name. That way all your email hits us and we can redirect it wherever you want. We make it easy to manage a single domain or a bunch of domains. Many domain registrars offer this service for a fee, and have clumsy management tools. We provide a robust simple toolset for free, as well as premium options).

The goal of the landing page is to get folks into the signup flow. The second priority flow is to have them take a look at the premium plan offerings.

We may offer the winning designer additional work for the remainder of the site design.
Updates

I've changed this project to a committed payment.  It is no longer refundable.  Thank you.

Target Market(s)

Bloggers, podcasters, designers, app developers - people who are a little tech savvy.

Industry/Entity Type

It Company

Font styles to use
Sans Serif

Colors

Designer to choose colors to be used in the design.

Requirements
Must have
• A full fidelity mockup (comp) of the landing page including the source file (psd, ai, etc).

Some sort of logo treatment for the ravo.qt brand

A call to action for signup, such as the suggested 'Get Started Here'
Nice to have
• A hip startup feel

Incorporation of the email theme

Give the impression it is simple, easy and fast

```html
<!DOCTYPE html>
<html lang="en">
<head>
<meta charset="utf-8">
<title>ravo.qt – email for your domain</title>
<link href="https://fonts.googleapis.com/css2?family=Signika:wght@300;400&family=Open+Sans:wght@400;600&display=swap" rel="stylesheet">
<style>
:root{
  --ink:#5a5a5a;
  --ink-soft:#777;
  --line:#e3e3e3;
  --orange-top:#ffa21a;
  --orange-bottom:#ff7a00;
  --orange-tab:#f06a0c;
  --dark-top:#2a2a2a;
  --dark-bottom:#050505;
  --sky:#26b7ef;
  --sky-dark:#1296d2;
  --footer:#454545;
  --footer-low:#626262;
  --gold:#e3b23c;
}
*{box-sizing:border-box;margin:0;padding:0}
html,body{width:1176px;height:1200px;overflow:hidden;background:#fff}
body{position:relative;font-family:"Signika",sans-serif;color:var(--ink)}

/* header */
.site-header{position:absolute;left:0;top:0;width:1176px;height:58px;background:#fff;border-bottom:1px solid var(--line);box-shadow:0 2px 3px rgba(0,0,0,.05)}
.brand{position:absolute;left:108px;top:6px;font-family:"Open Sans",sans-serif;font-size:31px;font-weight:400;color:#6f6f6f;letter-spacing:.5px}
.top-nav{position:absolute;right:124px;top:22px;font-size:14px;color:#6a6a6a;font-family:"Open Sans",sans-serif}
.top-nav span.sep{margin:0 12px}

/* hero */
.hero{position:absolute;left:0;top:59px;width:1176px;height:408px;background:linear-gradient(90deg,#f1f3f4 0%,#eef1f3 35%,#e6ebee 100%)}
.hero-photo{position:absolute;left:440px;top:0;width:736px;height:408px;background:linear-gradient(90deg,rgba(238,241,243,0) 0%,#d7dde2 25%,#c7d4de 55%,#a9c6e0 80%,#bcd3e6 100%)}
.hero-points{position:absolute;left:100px;top:110px;width:380px;list-style:none;text-align:right;font-size:18px;font-weight:300;color:#555;line-height:21px}
.hero-points li{position:relative;padding-right:20px;margin-bottom:20px}
.hero-points li::after{content:"";position:absolute;right:0;top:6px;width:7px;height:7px;border:1px solid #333;background:#fff;box-shadow:inset 0 0 0 2px #fff,inset 0 0 0 3px #333}

/* CTA band */
.cta-band{position:absolute;left:0;top:467px;width:1176px;height:88px;background:linear-gradient(#fff,#e9eff3)}
.cta{position:absolute;top:13px;width:322px;height:63px;border:2px solid #fff;box-shadow:0 0 0 1px #d6d6d6;display:flex;align-items:center;text-decoration:none;color:#fff;font-size:22px;font-weight:400}
.cta .tab{width:55px;height:100%;display:flex;align-items:center;justify-content:center}
.cta .label{padding-left:30px}
.cta-start{left:249px;background:linear-gradient(var(--orange-top),var(--orange-bottom))}
.cta-start .tab{background:var(--orange-tab)}
.cta-plans{left:602px;background:linear-gradient(var(--dark-top),var(--dark-bottom))}
.cta-plans .tab{background:linear-gradient(#8a8a8a,#6a6a6a)}

/* articles */
.article{position:absolute;top:604px;width:450px;height:290px}
.article .thumb{position:absolute;left:0;top:0;width:211px;height:130px;border:3px solid #e8e8e8;box-shadow:0 0 0 1px #ccc}
.article h2{position:absolute;left:222px;top:4px;width:240px;font-size:17px;font-weight:400;color:#5b5b5b;line-height:24px}
.article .lead,.article .rest{font-family:"Open Sans",sans-serif;font-size:11px;line-height:16px;color:#777;text-align:justify}
.article .lead{position:absolute;left:222px;width:228px}
.article .rest{position:absolute;left:3px;top:161px;width:446px}
.more{position:absolute;left:368px;top:236px;width:76px;height:30px;border-radius:3px;border:2px solid #c9ecfb;background:linear-gradient(var(--sky),var(--sky-dark));color:#fff;font-size:15px;text-align:center;line-height:26px}
.art-left{left:111px}
.art-right{left:611px}

/* footer */
.site-footer{position:absolute;left:0;top:909px;width:1176px;height:182px;background:var(--footer);border-top:3px solid #3a3a3a}
.seal{position:absolute;left:113px;top:30px;width:66px;height:66px;border-radius:50%;background:radial-gradient(#f2cc5c,var(--gold));border:3px solid #c98e1c}
.cards{position:absolute;left:191px;top:52px;display:flex;gap:9px}
.cards span{display:block;width:37px;height:24px;border:1px solid #888;border-radius:2px}
.trust{position:absolute;left:124px;font-family:"Open Sans",sans-serif;font-size:10.5px;letter-spacing:1px;color:#cfcfcf;display:flex;align-items:center;gap:14px}
.connect-title{position:absolute;right:106px;top:28px;font-size:20px;font-weight:300;color:#e6e6e6}
.social{position:absolute;font-size:13px;font-weight:300;color:#dedede;display:flex;align-items:center;gap:12px;justify-content:flex-end}
.social i{display:block;width:20px;height:20px;border-radius:2px}

.footer-base{position:absolute;left:0;top:1091px;width:1176px;height:109px;background:linear-gradient(#6a6a6a,var(--footer-low) 60%,#5a5a5a);text-align:center;color:#ececec;font-family:"Open Sans",sans-serif}
.footer-base p{position:absolute;left:0;width:100%}
.footer-base .sep{margin:0 9px}
</style>
</head>
<body>

<header class="site-header">
  <div class="brand">ravo.qt</div>
  <nav class="top-nav">How it works<span class="sep">|</span>Support<span class="sep">|</span>Login</nav>
</header>

<section class="hero">
  <div class="hero-photo" role="img" aria-label="Photo of a smiling businessman in a light blue shirt with blurred colleagues in an office behind him"></div>
  <ul class="hero-points">
    <li>We make email easy</li>
    <li>Give us five minutes and we’ll get you email from your domain</li>
    <li>Easily forward mail from your custom domain name wherever you want it</li>
    <li>You take the mail, we’ll keep the spam</li>
  </ul>
</section>

<section class="cta-band">
  <a class="cta cta-start" href="#">
    <span class="tab"><svg width="30" height="30" viewBox="0 0 30 30"><circle cx="15" cy="15" r="14" fill="#f9a25e"/><path d="M8 15h12M15 9l6 6-6 6" stroke="#e0600a" stroke-width="3" fill="none" stroke-linecap="round" stroke-linejoin="round"/></svg></span>
    <span class="label">GET STARTED HERE</span>
  </a>
  <a class="cta cta-plans" href="#">
    <span class="tab"><svg width="30" height="30" viewBox="0 0 30 30"><circle cx="15" cy="15" r="14" fill="#b5b5b5"/><path d="M8 15h12M15 9l6 6-6 6" stroke="#5a5a5a" stroke-width="3" fill="none" stroke-linecap="round" stroke-linejoin="round"/></svg></span>
    <span class="label">COMPARE PLANS</span>
  </a>
</section>

<article class="article art-left">
  <div class="thumb" role="img" aria-label="Illustration of a hand touching a glowing network of device icons" style="background:linear-gradient(120deg,#c9d2da,#6c7680 55%,#2b3138)"></div>
  <h2>How to configure your SkyVeilDNS to use ravo.qt</h2>
  <p class="lead" style="top:60px">Sed ut perspiciatis unde omnis iste natus error sit voluptatem accusantium doloremque laudantium, toram rem aperiam, eaque ipsa quae ab illo inventore veritatis et quasi architecto beatae vitae</p>
  <p class="rest">voluptatem quia voluptas sit aspernatur aut odit aut fugit, sed quiaSed ut perspiciatis unde omnis iste natus error sit voluptatem accusantium doloremque laudantium, toram rem aperiam, eaque ipsa quae ab illo inventore veritatis et quasi architecto beatae vitae dicta sunt explicabo. Sed ut perspiciatis unde omnis iste natus error sit voluptatem.</p>
  <div class="more">More</div>
</article>

<article class="article art-right">
  <div class="thumb" role="img" aria-label="Illustration of hands on a tablet with envelope icons floating upward" style="background:linear-gradient(160deg,#1c1c1c,#3a3a3a 60%,#8a8a8a)"></div>
  <h2>Use ravo.qt with your DomainBarn.domain registration for reliable email forwarding</h2>
  <p class="lead" style="top:84px">Sed ut perspiciatis unde omnis iste natus error sit voluptatem accusantium doloremque laudantium, toram rem aperiam, eaque ipsa quae inventore.</p>
  <p class="rest">voluptatem quia voluptas sit aspernatur aut odit aut fugit, sed quiaSed ut perspiciatis unde omnis iste natus error sit voluptatem accusantium doloremque laudantium, toram rem aperiam, eaque ipsa quae ab illo inventore veritatis et quasi architecto beatae vitae dicta sunt explicabo. Sed ut perspiciatis unde omnis iste natus error sit voluptatem.</p>
  <div class="more">More</div>
</article>

<footer class="site-footer">
  <div class="seal"></div>
  <div class="cards">
    <span style="background:#dfe6ee"></span>
    <span style="background:#e9edf3"></span>
    <span style="background:#1d3f8f"></span>
    <span style="background:#e8e8e8"></span>
    <span style="background:#5a76c8;margin-left:4px"></span>
    <span style="background:#11805a"></span>
    <span style="background:#a01e9a"></span>
  </div>
  <div class="trust" style="top:114px">
    <svg width="16" height="18" viewBox="0 0 16 18"><path d="M4 8V5a4 4 0 0 1 8 0v3" stroke="#e0a21e" stroke-width="2" fill="none"/><rect x="1" y="8" width="14" height="10" rx="2" fill="#f0b32a"/></svg>
    Secure and safe online shopping
  </div>
  <div class="trust" style="top:145px">
    <svg width="18" height="16" viewBox="0 0 18 16"><path d="M9 16V8M9 9C9 4 4 3 1 4c1 4 5 5 8 5zM9 9c0-5 5-6 8-5-1 4-5 5-8 5z" fill="#7ab53a" stroke="#7ab53a" stroke-width="1.5"/></svg>
    Guaranteed Fresh Product
  </div>

  <div class="connect-title">Connect with us</div>
  <div class="social" style="right:218px;top:72px">Pagebook<i style="background:#3b5a9a"></i></div>
  <div class="social" style="right:106px;top:72px">WorkLink<i style="background:#1a7fb7"></i></div>
  <div class="social" style="right:218px;top:107px">Chirply<i style="background:#3fb9e8"></i></div>
  <div class="social" style="right:106px;top:107px">Searchly +1<i style="background:#d6492f"></i></div>
  <div class="social" style="right:218px;top:142px">RSS<i style="background:#f27a1a"></i></div>
  <div class="social" style="right:106px;top:142px">Pinboardly<i style="background:#d22229;border-radius:50%"></i></div>
</footer>

<div class="footer-base">
  <p style="top:24px;font-size:12px">How it works<span class="sep">|</span>Support<span class="sep">|</span>Login<span class="sep">|</span>Contact</p>
  <p style="top:51px;font-size:13px">Privacy <span style="margin:0 2px">|</span> Disclaimer <span style="margin:0 2px">|</span> Terms &amp; Conditions</p>
  <p style="top:78px;font-size:13px">© 2014 ravo.qt. All rights reserved</p>
</div>

</body>
</html>
```